Brimvale Crest Homes needs a business card

We need a business card for a new company in Canada, Ontario. Our company is all about luxury contraction homes for our clients. Our product and services are custom projects design. Under the business logo that will be created, we want a slogan that will be a memorable phrase for consumers to remember us to tell their friends and relatives.

Additional infomation
- Teodoro Vanlesky
- President / Ceo
-519.304.7718

Find point what luxury construction products and services can be done

We like to see colors:
- #663300
- and something other colors or color that would attract the client needs and wants

The final design should communicate leads from new or old clients that will grow our empire. Most of all, we try to work among the budget that clients want

NOTE
- we also need an icon for the business (Example: Instagram, Facebook, and Whatsapp icons)
- We want the company name to be remembered easily for clients and our distributors who would get our orders.
- we need an icon on the business cards: Facebook and Instagram.

Thanks,
Brimvale Crest Homes

```html
<!DOCTYPE html>
<html lang="en">
<head>
<meta charset="utf-8">
<title>Brimvale Crest Homes – Business Card</title>
<link rel="stylesheet" href="https://fonts.googleapis.com/css2?family=Questrial&display=swap">
<style>
  :root {
    --bg: #1a1a1a;
    --card: #0c0c0c;
    --card-edge: #222222;
    --brown: #663300;
    --copper: #8a4a1c;
    --ink: #d9d9d9;
    --muted: #a8a8a8;
  }
  * { margin: 0; padding: 0; box-sizing: border-box; }
  html, body { width: 1200px; height: 900px; overflow: hidden; }
  body {
    background: radial-gradient(ellipse at 50% 40%, #222 0%, var(--bg) 70%);
    font-family: "Questrial", "Century Gothic", sans-serif;
    color: var(--ink);
    position: relative;
  }
  .card {
    position: absolute;
    width: 500px;
    height: 286px;
    background: var(--card);
    border-radius: 22px;
    border: 1px solid var(--card-edge);
    box-shadow: 0 18px 40px rgba(0,0,0,.55);
    overflow: hidden;
  }
  .card--front { left: 70px; top: 360px; }
  .card--back  { left: 630px; top: 90px; }

  /* front */
  .holder { position: absolute; left: 40px; top: 36px; }
  .holder__name { font-size: 28px; letter-spacing: .5px; color: var(--ink); }
  .holder__title { font-size: 13px; color: var(--copper); margin-top: 4px; letter-spacing: .3px; }
  .divider {
    position: absolute; left: 40px; top: 104px; width: 270px; height: 1px;
    background: var(--copper);
  }
  .contact { position: absolute; left: 40px; top: 150px; list-style: none; font-size: 13px; }
  .contact li { display: flex; align-items: center; gap: 9px; margin-bottom: 9px; }
  .contact svg { width: 12px; height: 12px; fill: var(--copper); }
  .brand {
    position: absolute; display: flex; align-items: center; gap: 10px;
    color: var(--ink); letter-spacing: 1.5px; text-transform: uppercase;
  }
  .brand__mark { width: 14px; height: 14px; background: var(--brown); }
  .card--front .brand { right: 32px; top: 96px; font-size: 15px; }
  .services-line {
    position: absolute; left: 40px; bottom: 30px;
    font-size: 12.5px; letter-spacing: 1px; color: var(--brown); text-transform: uppercase;
  }

  /* back */
  .offer { position: absolute; left: 40px; top: 32px; list-style: none; font-size: 13px; color: var(--muted); }
  .offer li { display: flex; align-items: center; gap: 8px; margin-bottom: 6px; }
  .offer svg { width: 11px; height: 11px; }
  .offer path { fill: none; stroke: var(--copper); stroke-width: 3; }
  .card--back .brand { right: 32px; bottom: 36px; font-size: 16px; }

  /* lockup */
  .lockup {
    position: absolute; right: 50px; bottom: 50px;
    display: flex; flex-direction: column; align-items: center; gap: 14px;
  }
  .lockup__mark { width: 60px; height: 60px; background: var(--brown); }
  .lockup__name { font-size: 26px; letter-spacing: 1.5px; color: #e6e6e6; text-transform: uppercase; }
</style>
</head>
<body>

<section class="card card--back" aria-label="Business card back">
  <ul class="offer">
    <li><svg viewBox="0 0 12 12"><path d="M1 6l3.5 3.5L11 2"/></svg>Custom Project Designs</li>
    <li><svg viewBox="0 0 12 12"><path d="M1 6l3.5 3.5L11 2"/></svg>Home Renovations</li>
    <li><svg viewBox="0 0 12 12"><path d="M1 6l3.5 3.5L11 2"/></svg>Kitchen remodeling</li>
    <li><svg viewBox="0 0 12 12"><path d="M1 6l3.5 3.5L11 2"/></svg>Extiror Design / Interior Design</li>
    <li><svg viewBox="0 0 12 12"><path d="M1 6l3.5 3.5L11 2"/></svg>Additions</li>
    <li><svg viewBox="0 0 12 12"><path d="M1 6l3.5 3.5L11 2"/></svg>Garages</li>
    <li><svg viewBox="0 0 12 12"><path d="M1 6l3.5 3.5L11 2"/></svg>Basements &amp; Bathrooms</li>
  </ul>
  <div class="brand"><span class="brand__mark"></span>Brimvale Crest Homes</div>
</section>

<section class="card card--front" aria-label="Business card front">
  <div class="holder">
    <p class="holder__name">Teodoro Vanlesky</p>
    <p class="holder__title">President / Ceo</p>
  </div>
  <div class="divider"></div>
  <div class="brand"><span class="brand__mark"></span>Brimvale Crest Homes</div>
  <ul class="contact">
    <li><svg viewBox="0 0 24 24"><path d="M6.6 10.8a15.1 15.1 0 006.6 6.6l2.2-2.2a1 1 0 011-.25 11.4 11.4 0 003.6.57 1 1 0 011 1V20a1 1 0 01-1 1A17 17 0 013 4a1 1 0 011-1h3.5a1 1 0 011 1 11.4 11.4 0 00.57 3.6 1 1 0 01-.25 1z"/></svg>519.304.7718</li>
    <li><svg viewBox="0 0 24 24"><path d="M2 5h20v14H2z M2 5l10 8 10-8" /></svg>hello@brimvalecrest.ca</li>
  </ul>
  <p class="services-line">Home Renovations &nbsp;|&nbsp; Custom Project Design</p>
</section>

<div class="lockup">
  <span class="lockup__mark"></span>
  <span class="lockup__name">Brimvale Crest Homes</span>
</div>

</body>
</html>
```